2 Funky Pages + EASY stock logo = Construction Website

We would like a funky new website - Just 2 pages - to promote our project management company. A logo is also needed, but we'll provide a stock image which just needs a colour change a text added.

Here are the instructions:

"Fair Tally Homes"

#logo
The one I'd like is attached. Please change font and positioning of text though.

Tagline is "Don't be normal - Be clever"

#Colour combo
756897 Wood Veneer
D5D6D2 sand dollar
353C3F charcoal
962715 brick red

#Home - Page 1

Our cost-price home build service will save you thousands.
No, seriously - Here's how we do it (button)

- Pay what the home building companies do.
- FTH will manage the entire project.
- Use Keystonecraft Guaranteed builders and materials.
- Tender for the best industry rates.
- Get a full budget calculated for the build.
- Avoid inflated 'Fixed-price' builds.
See how it works (button)

Contact Us: 0800 615 278
enquire - Name, Phone, email, comment - SEND

#How it works - Page 2

Traditional fixed price contracts are popular because it means that any risk of unexpected problems is carried by the home builder, but the builder will generally load the price about 10 times above the actual risk carried.

It's like an over-priced insurance policy, on steroids.

Clever people do things differently.

Here's how a cost-price build works...

1) Tell us what you want to build. Dream home, townhouse, investment property, whatever.

2) We'll put a design together for you, or you can choose from a bunch of plans we've already got.

3) We'll give you a conservative price estimate.

4) We finish tweaking your plans, then send them out to our network of more than 200 builders, subcontractors and tradesmen.

5) We collect the quotes, pick the best prices, and finalise your budget. Now you buy us beer, cause you've finally realised how much you're saving.

6) Tell your friends how awesome we are, while we lodge your building consent application with Council.

7) We coordinate the builders and subbies (look, you're already speaking trade-talk) from start to finish. You pay the cost price on their work each month.

We're happy to talk numbers and give you an estimate.

Contact Us: 0800 615 278

Reason: I have seen some great design elements, but need them to come together in one site design. Also, there appears to be less attention paid to the second page design ('how it works') than is necessary... There is no viable contender there yet, compared with the great home page submissions. I've also added some further info to the brief, and note that many submissions have ignored the colour combo I've requested.

Industry/Entity Type

Construction

Number of Pages Required

2 page

Requirements
Must have
• Keystonecrafter logo (small)
• Colour combo described in brief.
Nice to have
• I've attached a stock image I like, but it's certainly not essential. I do like images with clear backgrounds though - they tend to produce a crisp looking site.
• There is a wider image similar to this, available on Pixel Vault, but Sketch Hive won't let me attach it.
Should not have
• Photos of cheesy American faces.

```html
<!DOCTYPE html>
<html lang="en">
<head>
<meta charset="utf-8">
<title>Fair Tally Homes — How it works</title>
<link href="https://fonts.googleapis.com/css2?family=Open+Sans:wght@400;600&family=Dancing+Script:wght@500&display=swap" rel="stylesheet">
<style>
:root{
  --wood:#756897;
  --sand:#d5d6d2;
  --charcoal:#353c3f;
  --brick:#962715;
  --ink:#333333;
  --muted:#8a8a8a;
  --panel-left:#f7f7f7;
  --panel-right:#efefef;
  --footer:#2b2b30;
  --logo-box:#3d3d3f;
  --sky-top:#3a84c9;
  --sky-bottom:#a9cbe6;
}
*{box-sizing:border-box;margin:0;padding:0}
html,body{width:927px;height:1200px;overflow:hidden;background:#fff}
body{position:relative;font-family:"Open Sans",Arial,sans-serif;color:var(--ink)}
.abs{position:absolute}

/* hero */
.hero{left:0;top:0;width:927px;height:333px;
  background:linear-gradient(180deg,var(--sky-top) 0%,var(--sky-bottom) 100%)}
.logo{left:102px;top:0;width:131px;height:130px;background:var(--logo-box);
  display:flex;align-items:center;justify-content:center;flex-direction:column;gap:8px}
.logo-mark{width:14px;height:14px;background:#c9d52b}
.logo-name{color:#ffffff;font-size:11px;font-weight:600;letter-spacing:.3px}
.nav{top:12px;left:535px;display:flex;gap:16px;font-size:8.5px;color:#fff}
.nav a{color:#fff;text-decoration:none;padding-bottom:2px}
.nav a.active{border-bottom:1px solid #fff}
.tagline{left:142px;top:166px;font-family:"Dancing Script",cursive;font-size:36px;color:#1b1b1b;white-space:nowrap}
.dots{left:433px;top:312px;width:60px;height:14px;border-radius:7px;background:rgba(40,40,40,.55);
  display:flex;align-items:center;justify-content:center;gap:6px}
.dots i{width:6px;height:6px;border-radius:50%;background:#fff;display:block}
.dots i:first-child{background:transparent;border:1px solid #fff}

/* intro */
.intro{left:100px;top:364px;width:727px;text-align:center;font-size:11.2px;line-height:17.5px;color:var(--ink)}
.lead-line{left:0;width:927px;text-align:center;font-size:10px;color:var(--wood)}

/* steps */
.step-icon{width:26px;height:26px}
.step-text{font-size:11.2px;line-height:16px;color:var(--brick);text-align:justify}
.left-col{left:134px;width:301px}
.right-col{left:517px;width:301px}
.arrow{stroke:var(--wood);stroke-width:2;fill:none;stroke-linecap:round;stroke-linejoin:round}
.closing{left:100px;top:817px;width:727px;text-align:center;font-size:11.2px;line-height:16px;color:var(--brick)}
.cta-line{left:0;top:868px;width:927px;text-align:center;font-size:14.5px;color:#222}

/* contact */
.contact-left{left:0;top:916px;width:463px;height:185px;background:var(--panel-left)}
.contact-right{left:463px;top:916px;width:464px;height:185px;background:var(--panel-right)}
.phone-ring{left:106px;top:952px;width:31px;height:31px;border-radius:50%;border:1px solid #dcdcdc;background:#fff;
  display:flex;align-items:center;justify-content:center}
.contact-label{left:145px;top:947px;font-size:13.5px;color:var(--brick)}
.contact-number{left:145px;top:959px;font-size:22px;font-weight:600;color:var(--brick);letter-spacing:.2px}
.contact-copy{left:105px;top:996px;width:340px;font-size:8.8px;line-height:16px;color:var(--muted)}
.enquire-title{left:484px;top:946px;font-size:15.5px;color:var(--wood)}
.field{background:#fff;border:1px solid #dedede;font-size:7.5px;color:#a5a5a5;padding:0 10px;display:flex;align-items:center}
.send{left:486px;top:1044px;width:45px;height:25px;background:var(--charcoal);color:#fff;font-size:8px;
  display:flex;align-items:center;justify-content:center;letter-spacing:.3px}

/* footer */
.footer{left:0;top:1101px;width:927px;height:99px;background:var(--footer)}
.social{left:102px;top:1119px;display:flex;gap:16px;align-items:center}
.social i{display:block;width:10px;height:10px;border-radius:50%;background:#8c8c8f}
.footer-links{left:102px;top:1146px;font-size:8.8px;color:#8c8c8f;word-spacing:2px}
.copyright{left:102px;top:1166px;font-size:8.8px;color:#8c8c8f}
.badge{left:768px;top:1115px;width:57px;height:57px;background:#59595c}
</style>
</head>
<body>

<header>
  <div class="abs hero" role="img" aria-label="Photo of a brick family house with a tiled roof under a blue sky, with green fields and trees"></div>
  <div class="abs logo"><span class="logo-mark"></span><span class="logo-name">Fair Tally Homes</span></div>
  <nav class="abs nav">
    <a href="#">Home</a><a href="#">About us</a><a href="#" class="active">How it works</a><a href="#">Services</a><a href="#">Projects</a><a href="#">Contact us</a>
  </nav>
  <div class="abs tagline">Don't be normal – Be clever</div>
  <div class="abs dots"><i></i><i></i><i></i><i></i></div>
</header>

<main>
  <p class="abs intro">Traditional fixed price contracts are popular because it means that any risk of unexpected problems is carried by the home builder, but the builder will generally load the price about 10 times above the actual risk carried.</p>
  <p class="abs lead-line" style="top:406px">It's like an over-priced insurance policy, on steroids.</p>
  <p class="abs lead-line" style="top:428px">Clever people do things differently.</p>
  <p class="abs lead-line" style="top:450px">Here's how a cost-price build works...</p>

  <svg class="abs step-icon" style="left:101px;top:497px" viewBox="0 0 26 26"><path d="M13 4C6.5 4 2 7.6 2 12c0 2.4 1.3 4.5 3.5 5.9L4 23l5.6-3.3c1.1.3 2.2.4 3.4.4 6.5 0 11-3.6 11-8S19.5 4 13 4z" fill="var(--brick)"/></svg>
  <p class="abs step-text left-col" style="top:495px">Tell us what you want to build. Dream home, townhouse, investment property, whatever.</p>
  <svg class="abs" style="left:445px;top:495px" width="26" height="24" viewBox="0 0 26 24"><path class="arrow" d="M3 12h20M15 4l8 8-8 8"/></svg>

  <svg class="abs step-icon" style="left:485px;top:495px" viewBox="0 0 26 26"><g fill="none" stroke="var(--brick)" stroke-width="1.8"><path d="M3 9l6-6h6v14H3z"/><path d="M11 11l6-6h6v18H11z" fill="#fff"/></g></svg>
  <p class="abs step-text right-col" style="top:495px">We'll put a design together for you, or you can choose from a bunch of plans we've already got.</p>
  <svg class="abs" style="left:486px;top:538px" width="24" height="26" viewBox="0 0 24 26"><path class="arrow" d="M12 3v20M4 15l8 8 8-8"/></svg>

  <svg class="abs step-icon" style="left:485px;top:577px" viewBox="0 0 26 26"><g fill="var(--brick)"><rect x="2" y="23" width="23" height="1.6"/><rect x="2" y="3" width="1.6" height="21"/><rect x="6" y="13" width="2.4" height="9"/><rect x="10" y="16" width="2.4" height="6"/><rect x="14" y="10" width="2.4" height="12"/><rect x="18" y="14" width="2.4" height="8"/><rect x="22" y="7" width="2.4" height="15"/></g></svg>
  <p class="abs step-text right-col" style="top:575px">We'll give you a conservative price estimate.</p>
  <svg class="abs" style="left:445px;top:578px" width="26" height="24" viewBox="0 0 26 24"><path class="arrow" d="M23 12H3M11 4l-8 8 8 8"/></svg>

  <svg class="abs step-icon" style="left:101px;top:576px" viewBox="0 0 26 26"><g fill="none" stroke="var(--brick)" stroke-width="1.8"><rect x="2" y="5" width="22" height="16" rx="1.5"/><path d="M2.5 6l10.5 9 10.5-9"/></g></svg>
  <p class="abs step-text left-col" style="top:575px">We finish tweaking your plans, then send them out to our network of more than 200 builders, subcontractors and tradesmen.</p>
  <svg class="abs" style="left:101px;top:621px" width="24" height="26" viewBox="0 0 24 26"><path class="arrow" d="M12 3v20M4 15l8 8 8-8"/></svg>

  <svg class="abs step-icon" style="left:103px;top:670px" viewBox="0 0 26 26"><circle cx="13" cy="13" r="10.5" fill="none" stroke="var(--brick)" stroke-width="2.4"/><path d="M8 13l3.6 3.6L18.5 9.5" fill="none" stroke="var(--brick)" stroke-width="2.6" stroke-linecap="round" stroke-linejoin="round"/></svg>
  <p class="abs step-text left-col" style="top:668px">We collect the quotes, pick the best prices, and finalise your budget. Now you buy us beer, cause you've finally realised how much you're saving.</p>
  <svg class="abs" style="left:445px;top:670px" width="26" height="24" viewBox="0 0 26 24"><path class="arrow" d="M3 12h20M15 4l8 8-8 8"/></svg>

  <svg class="abs step-icon" style="left:483px;top:668px" viewBox="0 0 28 26"><g fill="var(--brick)"><circle cx="14" cy="6" r="4"/><circle cx="6" cy="9" r="3"/><circle cx="22" cy="9" r="3"/><path d="M7 24v-5c0-3 3-6 7-6s7 3 7 6v5z"/><path d="M1 22v-3c0-2 2-4 5-4 1 0 2 .3 2 .5-1 1-1.5 2.4-1.5 3.5V22z"/><path d="M27 22v-3c0-2-2-4-5-4-1 0-2 .3-2 .5 1 1 1.5 2.4 1.5 3.5V22z"/></g></svg>
  <p class="abs step-text right-col" style="top:668px">Tell your friends how awesome we are, while we lodge your building consent application with Council.</p>
  <svg class="abs" style="left:482px;top:708px" width="22" height="76" viewBox="0 0 22 76"><path class="arrow" stroke-width="1.6" d="M17 2v68H4M10 63l-6 7 6 7"/></svg>

  <svg class="abs" style="left:446px;top:761px" width="34" height="32" viewBox="0 0 34 32"><g fill="var(--brick)"><circle cx="12" cy="18" r="7.5"/><g transform="translate(12 18)"><rect x="-2.2" y="-11" width="4.4" height="22"/><rect x="-11" y="-2.2" width="22" height="4.4"/><rect x="-2.2" y="-11" width="4.4" height="22" transform="rotate(45)"/><rect x="-2.2" y="-11" width="4.4" height="22" transform="rotate(-45)"/></g><circle cx="26" cy="8" r="4.5"/><g transform="translate(26 8)"><rect x="-1.5" y="-7" width="3" height="14"/><rect x="-7" y="-1.5" width="14" height="3"/></g><circle cx="26" cy="25" r="4"/><g transform="translate(26 25)"><rect x="-1.4" y="-6.5" width="2.8" height="13"/><rect x="-6.5" y="-1.4" width="13" height="2.8"/></g></g><circle cx="12" cy="18" r="2.6" fill="#fff"/><circle cx="26" cy="8" r="1.6" fill="#fff"/><circle cx="26" cy="25" r="1.4" fill="#fff"/></svg>
  <p class="abs closing">We coordinate the builders and subbies (look, you're already speaking trade-talk) from start to finish. You pay the cost price on their work each month.</p>

  <p class="abs cta-line">We're happy to talk numbers and give you an estimate.</p>
</main>

<section>
  <div class="abs contact-left"></div>
  <div class="abs contact-right"></div>
  <div class="abs phone-ring"><svg width="12" height="12" viewBox="0 0 24 24"><path d="M6.6 10.8c1.4 2.8 3.8 5.1 6.6 6.6l2.2-2.2c.3-.3.7-.4 1-.2 1.1.4 2.3.6 3.6.6.6 0 1 .4 1 1V20c0 .6-.4 1-1 1C10.6 21 3 13.4 3 4c0-.6.4-1 1-1h3.5c.6 0 1 .4 1 1 0 1.2.2 2.4.6 3.6.1.3 0 .7-.2 1z" fill="#a9a9a9"/></svg></div>
  <div class="abs contact-label">Contact Us</div>
  <div class="abs contact-number">0800 615 278</div>
  <p class="abs contact-copy">Cras neque mi, ultricies id orci sed, maximus luctus elit. Nulla posuere, sapien sed sodales imperdiet, purus libero laoreet est, eu rutrum ante erat et urna. Proin vitae diam dictum, volutpat diam vel, porttitor elit. Morbi lacinia sapien risus, sit amet ultricies metus accumsan sed.</p>

  <div class="abs enquire-title">Enquire</div>
  <div class="abs field" style="left:486px;top:974px;width:106px;height:25px">Name</div>
  <div class="abs field" style="left:602px;top:974px;width:106px;height:25px">Phone</div>
  <div class="abs field" style="left:719px;top:974px;width:105px;height:25px">Email</div>
  <div class="abs field" style="left:486px;top:1008px;width:338px;height:26px">Comment</div>
  <div class="abs send">SEND</div>
</section>

<footer>
  <div class="abs footer"></div>
  <div class="abs social">
    <i></i><i></i><i></i><i></i>
    <svg width="13" height="10" viewBox="0 0 26 20"><rect x="0" y="0" width="26" height="20" rx="2" fill="#8c8c8f"/><path d="M1 2l12 9 12-9" fill="none" stroke="#2b2b30" stroke-width="2"/></svg>
  </div>
  <div class="abs footer-links">Home &nbsp;| &nbsp;About us &nbsp;| &nbsp;How it works &nbsp;| &nbsp;Services &nbsp;| &nbsp;Projects &nbsp;| &nbsp;Contact us</div>
  <div class="abs copyright">Copyright &nbsp;© &nbsp;2016 &nbsp;Fair Tally Homes. &nbsp;All rights reserved.</div>
  <div class="abs badge" role="img" aria-label="Keystonecrafter membership badge"></div>
</footer>

</body>
</html>
```